Employee I.D. Card - Badge

We need an employee I.D. card designed. Our employees are going to be wearing these. I would like to have it look nice. Something professional yet cool (not uptight if that makes sense).
Project Scope:
Vertical orientation
Company name ------------- (Bright and Tidy)
Website ------------- (brightandtidymn.example)
Employee Picture
background check image
front and back designed - same design on either side
You can create the card without having the employee images on them.
Here are the dimensions -
2.125 x 3.370 inches
Double sided - same design can be used front and back
Background badge - I would like to add an image that shows that the employee has taken a background check. I've added the press-kit for the company we use. If you have a better idea than incorporating their logo, we can certainly do something different.
Example image-
https://www.lookupzone.example/find?q=background+check+badge&kind=images&ref=XyZ4qWm82LpRt:
The print company will set up the names.
Logo is attached
Also attached are our business cards. You can use this for an idea of brand/company style.
Our website - brightandtidymn.example

```html
<!DOCTYPE html>
<html lang="en">
<head>
<meta charset="utf-8">
<title>Bright and Tidy — Employee ID Badge</title>
<link rel="stylesheet" href="https://fonts.googleapis.com/css2?family=Open+Sans:wght@400;600&display=swap">
<style>
  :root {
    --page-bg: #ecedef;
    --navy: #1f2a56;
    --sky-start: #00b5ee;
    --sky-end: #0b72bc;
    --stripe-grey: #c3c4c8;
    --stripe-blue: #48c6ef;
    --stripe-lime: #d3df4e;
    --brand-blue: #1ba3df;
    --photo-bg: #d1d2d4;
    --photo-fill: #76777a;
    --seal-ring: #0b0b0b;
    --seal-core: #7cc142;
    --white: #ffffff;
  }
  * { margin: 0; padding: 0; box-sizing: border-box; }
  html, body {
    width: 1200px;
    height: 1107px;
    overflow: hidden;
    background: var(--page-bg);
    font-family: "Open Sans", Arial, sans-serif;
  }
  .canvas {
    position: relative;
    width: 1200px;
    height: 1107px;
  }
  .id-card {
    position: absolute;
    left: 320px;
    top: 110px;
    width: 560px;
    height: 888px;
    border-radius: 20px;
    overflow: hidden;
    background: linear-gradient(90deg, var(--sky-start) 0%, var(--sky-start) 40%, var(--sky-end) 100%);
    box-shadow: 0 6px 18px rgba(0, 0, 0, 0.12);
  }
  .id-card__top {
    position: absolute;
    left: 0;
    top: 0;
    width: 100%;
    height: 497px;
    background: var(--navy);
  }
  .edge-stripe {
    position: absolute;
    left: 0;
    top: 0;
    width: 32px;
    height: 756px;
    display: flex;
    flex-direction: column;
  }
  .edge-stripe__grey { height: 251px; background: var(--stripe-grey); }
  .edge-stripe__blue { height: 247px; background: var(--stripe-blue); }
  .edge-stripe__lime { height: 258px; background: var(--stripe-lime); }
  .brand-name {
    position: absolute;
    left: 32px;
    right: 0;
    top: 70px;
    text-align: center;
    font-weight: 400;
    font-size: 66px;
    line-height: 1;
    letter-spacing: -1px;
    color: var(--brand-blue);
  }
  .website {
    position: absolute;
    left: 32px;
    right: 0;
    top: 270px;
    text-align: center;
    font-weight: 400;
    font-size: 31px;
    color: var(--white);
    letter-spacing: 0.2px;
  }
  .photo-slot {
    position: absolute;
    left: 120px;
    top: 345px;
    width: 333px;
    height: 396px;
    border-radius: 16px;
    border: 3px solid var(--navy);
    background: linear-gradient(180deg, var(--photo-bg) 0%, var(--photo-bg) 45%, #a9aaad 100%);
  }
  .clearance-seal {
    position: absolute;
    left: 339px;
    top: 662px;
    width: 202px;
    height: 202px;
  }
</style>
</head>
<body>
<main class="canvas">
  <section class="id-card" aria-label="Employee ID badge">
    <div class="id-card__top"></div>
    <div class="edge-stripe" aria-hidden="true">
      <span class="edge-stripe__grey"></span>
      <span class="edge-stripe__blue"></span>
      <span class="edge-stripe__lime"></span>
    </div>
    <h1 class="brand-name">Bright and Tidy</h1>
    <p class="website">www.brightandtidymn.example</p>
    <div class="photo-slot" role="img" aria-label="Employee photo placeholder"></div>
    <svg class="clearance-seal" viewBox="0 0 202 202" role="img" aria-label="Background check cleared seal">
      <circle cx="101" cy="101" r="100" fill="var(--seal-ring)"/>
      <circle cx="101" cy="101" r="56" fill="var(--seal-core)"/>
      <circle cx="101" cy="101" r="42" fill="none" stroke="var(--white)" stroke-width="4"/>
    </svg>
  </section>
</main>
</body>
</html>
```